Clikora - photography in NYC - leveraging big data and robotics

We've got a photography business in NYC. It is kind of on-demand photographers, but actually is just five of us who work as a team. Over the last three years we've taken tens of thousands of photographs and are now sitting on a load of great work. We want to leverage that in a way that lets people book either by event type or location. So, they would click on Harlow Green and a load of examples of our work would pop up. Or Wedding Shower, and relevant examples would pop up. We've got the pictures structured pretty well to enable this. Now we just need a website that illustrates this and then leads through the booking process (time, location, date, contact etc.) and payment.

Target Market(s)

Everyone - corporates, real estate, tourists, families, headshots, bloggers, products, wedding showers, baby showers, engagements, venues, restaurants/bars, holiday pictures, City Hall weddings, kids birthday parties, adult birthday parties, PR companies, corporate events.... long list.

Industry/Entity Type

Photographer

Number of Pages Required

5+ page

Colors

Designer to choose colors to be used in the design.

Requirements
Must have
• A great, engaging landing page which people can choose by event type or location. This would then pull in examples of our work in that location or in that event type. Then they go through the booking process. This is simple capturing key details - see here https://clikora.example/book/
Nice to have
• Social links
Should not have
• Nothing specific.

```html
<!DOCTYPE html>
<html lang="en">
<head>
<meta charset="utf-8">
<title>Clikora — Photography</title>
<link href="https://fonts.googleapis.com/css2?family=Crimson+Text:wght@400;600;700&family=Open+Sans:wght@400;600;700&display=swap" rel="stylesheet">
<style>
  :root{
    --stage:#dcdcdc;
    --page:#ffffff;
    --ink:#1e1e1e;
    --muted:#555555;
    --accent:#f7931e;
    --accent-soft:#fde9d2;
    --nav:#5a5a5a;
    --hero-a:#4d6a32;
    --hero-b:#2a2f26;
    --band:#2e332f;
    --footer:#3b3b3b;
    --footer-ink:#d8d8d8;
    --serif:"Crimson Text", Georgia, serif;
    --sans:"Open Sans", Arial, sans-serif;
  }
  *{box-sizing:border-box;margin:0;padding:0}
  html,body{width:1200px;height:1200px;overflow:hidden;background:var(--stage)}
  .stage{position:relative;width:1200px;height:1200px}
  .page{position:absolute;left:461px;top:12px;width:228px;height:965px;background:var(--page);
        transform:scale(1.22);transform-origin:0 0;font-family:var(--serif);color:var(--ink);overflow:hidden}
  .abs{position:absolute}
  .center{left:0;right:0;text-align:center}

  .hero{left:0;top:0;width:228px;height:152px;
        background:radial-gradient(ellipse at 60% 70%, #1c1d22 0 22%, transparent 45%),
                   linear-gradient(135deg,var(--hero-a),var(--hero-b) 70%)}
  .nav{left:0;top:0;width:228px;height:18px;background:var(--nav)}
  .nav .logo{left:16px;top:5px;font-size:7px;color:#fff;letter-spacing:.3px}
  .nav ul{list-style:none;position:absolute;left:68px;top:7px;display:flex;gap:12px;font-size:3.6px;color:#eee}
  .hero-title{top:52px;font-size:7.6px;line-height:10px;color:#fff;font-weight:400;letter-spacing:.2px}
  .btn{background:var(--accent);color:#fff;border-radius:6px;text-align:center;white-space:nowrap}
  .hero-btn{left:83px;top:83px;width:62px;height:11px;font-size:5.2px;line-height:11px}

  h2{font-weight:600;font-size:6.8px;text-align:center}
  .lede{font-size:3.2px;line-height:4.4px;text-align:center}
  .divider{height:.5px;background:#f3c69a;left:65px;width:98px}

  .filters{left:16px;top:271px;width:196px;display:flex;justify-content:center;align-items:center;gap:2px;font-family:var(--sans);font-size:2.6px;white-space:nowrap}
  .filters .label{color:var(--muted);font-weight:600;margin-right:1px}
  .filters .sep{width:.5px;height:5px;background:#ccc;margin:0 3px}
  .chip{padding:.8px 2.6px;border-radius:3px;border:.4px solid #d9d9d9;color:var(--ink)}
  .chip.on{background:var(--accent);border-color:var(--accent);color:#fff}

  .shot{position:absolute;width:63px}
  .shot span{position:absolute;left:2px;bottom:3px;font-size:3.2px;color:#fff;line-height:3.6px}
  .shot small{display:block;font-size:2.2px;font-family:var(--sans);color:#eee}

  .svc{position:absolute;width:56px}
  .svc .ico{width:20px;height:20px;border-radius:50%;background:var(--accent);margin:0 0 4px 12px;display:flex;align-items:center;justify-content:center}
  .svc b{display:block;font-size:3.6px;font-weight:600;margin-bottom:2px}
  .svc p{font-size:2.2px;line-height:3px;color:var(--muted)}
  .svc.active b{color:var(--accent);font-family:var(--sans)}
  .svc.active p{color:var(--ink);font-weight:700;font-family:var(--sans)}

  .band{left:0;top:632px;width:228px;height:106px;
        background:linear-gradient(180deg,#3d463c,var(--band) 60%,#23272a)}
  .stat{position:absolute;top:22px;width:50px;text-align:center;color:#fff}
  .stat b{display:block;font-family:var(--sans);font-size:6.4px;font-weight:600}
  .stat span{font-size:3px;color:#ddd}
  .steps{left:17px;top:56px;width:194px;display:flex;justify-content:space-between;align-items:center;font-family:var(--sans);font-size:2.6px;color:#eee;white-space:nowrap}
  .steps li{list-style:none;display:flex;align-items:center;gap:2px}
  .steps i{font-style:normal;width:5px;height:5px;border-radius:50%;background:var(--accent);color:#fff;font-size:2.6px;line-height:5px;text-align:center}
  .steps .line{flex:1;height:.4px;background:#777;margin:0 3px}
  .band .ask{left:17px;top:82px;font-size:5px;color:#fff}
  .band-btn{left:156px;top:82px;width:46px;height:9px;font-size:3.6px;line-height:9px}

  .avatar{position:absolute;border-radius:50%;background:linear-gradient(135deg,#8a6a58,#3a2c28)}
  .arrow{position:absolute;top:778px;font-size:8px;color:#888;font-family:var(--sans)}

  .footer{left:0;top:850px;width:228px;height:115px;background:var(--footer);color:var(--footer-ink)}
  .footer h3{font-size:4.4px;font-weight:400;margin-bottom:6px;color:#fff}
  .footer p,.footer li{font-size:2.8px;line-height:4px}
  .footer ul{list-style:none;font-family:var(--sans)}
  .social{display:flex;gap:2px;margin-top:3px}
  .social i{width:5px;height:5px;border-radius:50%;background:#fff;display:block}
  .footer .contact li{display:flex;gap:3px;align-items:flex-start;font-weight:700}
  .footer .logo{left:17px;top:100px;font-size:6px;color:#fff}
  .footer .copy{right:17px;top:102px;font-size:2.8px;font-family:var(--sans);font-weight:700;color:#fff}
</style>
</head>
<body>
<div class="stage">
  <main class="page">

    <section class="abs hero" role="img" aria-label="Hero photograph: camera lens resting outdoors against a blurred green background"></section>
    <header class="abs nav">
      <div class="abs logo">LOGO</div>
      <ul><li>Home</li><li>Portfolio</li><li>Service</li><li>Blog</li><li>Contact</li></ul>
    </header>
    <h1 class="abs center hero-title">Seeing the World, Through<br>the Eyes of My Lens</h1>
    <a class="abs btn hero-btn">View Portfolio</a>

    <section class="abs center" style="top:172px">
      <h2>About us.</h2>
      <p class="lede" style="width:160px;margin:8px auto 0">Lorem ipsum dolor sit amet, consectetur adipiscing elit, sed do eiusmod tempor incididunt ut labore et dolore magna aliqua. Ut enim ad minim veniam, quis nostrud exercitation ullamco laboris nisi ut aliquip ex ea commodo consequat. "Lorem ipsumexercitation ullamco laboris n.</p>
    </section>
    <div class="abs divider" style="top:241px"></div>

    <h2 class="abs center" style="top:257px">Portfolio</h2>
    <nav class="abs filters" aria-label="Browse work">
      <span class="label">Event:</span>
      <span class="chip on">Weddings</span><span class="chip">Birthdays</span><span class="chip">Corporate</span>
      <span class="sep"></span>
      <span class="label">Place:</span>
      <span class="chip">Harlow Green</span><span class="chip">City Hall</span><span class="chip">Midtown</span>
    </nav>
    <div class="shot" role="img" aria-label="Photographer holding a camera" style="left:16px;top:286px;height:45px;background:linear-gradient(135deg,#3a3d44,#15161a)"><span>Photography<small>Photo Shoot</small></span></div>
    <div class="shot" role="img" aria-label="Hiker on a rocky summit under blue sky" style="left:83px;top:286px;height:59px;background:linear-gradient(180deg,#6d9cc9,#c7c2b8)"></div>
    <div class="shot" role="img" aria-label="Landscape at dusk with mountain road" style="left:149px;top:286px;height:45px;background:linear-gradient(160deg,#5a5c4c,#2f3a2a)"><span>Landscape<small>Harlow Green</small></span></div>
    <div class="shot" role="img" aria-label="Camera mounted on a gimbal" style="left:16px;top:336px;height:60px;background:linear-gradient(135deg,#cfd2d6,#4a4c52)"></div>
    <div class="shot" role="img" aria-label="Traveller by a lake among green hills" style="left:83px;top:349px;height:47px;background:linear-gradient(180deg,#6e8a8e,#2f4a3a)"></div>
    <div class="shot" role="img" aria-label="City street at night with red lights" style="left:149px;top:336px;height:60px;background:linear-gradient(160deg,#2b3250,#7a2a3c)"></div>
    <div class="abs divider" style="top:419px"></div>

    <h2 class="abs center" style="top:439px">Services</h2>
    <div class="svc" style="left:16px;top:464px"><div class="ico"><svg width="10" height="10" viewBox="0 0 10 10" fill="none" stroke="#fff" stroke-width=".8"><circle cx="4" cy="6" r="2"/><circle cx="6" cy="4" r="2"/></svg></div><b>Wedding Shoots</b><p>Lorem ipsum dolor sit amet, consectetur adipiscing elit, sed do eiusmod tempor incididunt ut labore.</p></div>
    <div class="svc" style="left:95px;top:464px"><div class="ico"><svg width="10" height="10" viewBox="0 0 10 10" fill="none" stroke="#fff" stroke-width=".8"><rect x="1.5" y="2.5" width="7" height="5.5" rx="1"/><circle cx="5" cy="5.2" r="1.5"/></svg></div><b>Photo Shoot</b><p>Lorem ipsum dolor sit amet, consectetur adipiscing elit, sed do eiusmod tempor incididunt ut labore.</p></div>
    <div class="svc active" style="left:165px;top:464px"><div class="ico"><svg width="10" height="10" viewBox="0 0 10 10" fill="none" stroke="#fff" stroke-width=".8"><rect x="1.5" y="3" width="5" height="4" rx=".6"/><path d="M6.5 4.5L8.5 3.5V6.5L6.5 5.5"/></svg></div><b>Vedio &amp; Film</b><p>Lorem ipsum dolor sit amet, consectetur adipiscing elit, sed do eiusmod tempor incididunt ut labore et.</p></div>
    <div class="svc" style="left:16px;top:544px"><div class="ico"><svg width="10" height="10" viewBox="0 0 10 10" fill="none" stroke="#fff" stroke-width=".8"><rect x="2" y="2" width="6" height="6"/><path d="M3.5 2v6M6.5 2v6"/></svg></div><b>Vedio Production</b><p>Lorem ipsum dolor sit amet, consectetur adipiscing elit, sed do eiusmod tempor incididunt ut labore.</p></div>
    <div class="svc" style="left:95px;top:544px"><div class="ico"><svg width="10" height="10" viewBox="0 0 10 10" fill="none" stroke="#fff" stroke-width=".8"><rect x="2.5" y="4" width="2" height="4.5"/><rect x="5.5" y="4" width="2" height="4.5"/><path d="M3.5 4V2M6.5 4V2"/></svg></div><b>Makeup Shoots</b><p>Lorem ipsum dolor sit amet, consectetur adipiscing elit, sed do eiusmod tempor incididunt ut labore.</p></div>
    <div class="svc" style="left:165px;top:544px"><div class="ico"><svg width="10" height="10" viewBox="0 0 10 10" fill="none" stroke="#fff" stroke-width=".8"><path d="M2 8l2-5 2 2 2-3"/><circle cx="7.5" cy="7" r="1"/></svg></div><b>Fashion Shoots</b><p>Lorem ipsum dolor sit amet, consectetur adipiscing elit, sed do eiusmod tempor incididunt ut labore.</p></div>

    <section class="abs band" role="img" aria-label="Dim background photograph of a camera on a landscape">
      <div class="stat" style="left:13px"><b>30+</b><span>Year of Experience</span></div>
      <div class="stat" style="left:67px"><b>115+</b><span>Happy Client</span></div>
      <div class="stat" style="left:122px"><b>90+</b><span>Complete Project</span></div>
      <div class="stat" style="left:177px"><b>10+</b><span>Award Won</span></div>
      <ol class="abs steps" aria-label="Booking steps">
        <li><i>1</i>Event or place</li><span class="line"></span>
        <li><i>2</i>Date &amp; time</li><span class="line"></span>
        <li><i>3</i>Your details</li><span class="line"></span>
        <li><i>4</i>Payment</li>
      </ol>
      <div class="abs ask">Looking for Best Photographer?</div>
      <a class="abs btn band-btn">Book now</a>
    </section>

    <h2 class="abs center" style="top:751px">Testimonial</h2>
    <div class="arrow" style="left:17px">‹</div>
    <div class="arrow" style="left:207px">›</div>
    <div class="avatar" role="img" aria-label="Client portrait" style="left:34px;top:779px;width:10px;height:10px"></div>
    <div class="avatar" role="img" aria-label="Client portrait" style="left:69px;top:779px;width:10px;height:10px;background:linear-gradient(135deg,#c94a4a,#5a2a2a)"></div>
    <div class="avatar" role="img" aria-label="Featured client portrait" style="left:106px;top:775px;width:18px;height:18px;border:1px solid var(--accent);background:linear-gradient(135deg,#7a5a44,#1e1a18)"></div>
    <div class="avatar" role="img" aria-label="Client portrait" style="left:151px;top:779px;width:10px;height:10px;background:linear-gradient(135deg,#b58a6a,#4a3a30)"></div>
    <div class="avatar" role="img" aria-label="Client portrait" style="left:183px;top:779px;width:10px;height:10px;background:linear-gradient(135deg,#6a7a8a,#2a3238)"></div>
    <div class="abs center" style="top:803px;font-size:3.2px;color:var(--accent)">Nora Castell</div>
    <div class="abs center" style="top:808px;font-size:2.6px">Regular Client</div>
    <p class="abs lede" style="top:815px;width:110px;left:59px;font-size:2.6px;line-height:3.4px">"Lorem ipsum dolor sit amet, consectetur adipiscing elit, sed do eiusmod tempor incididunt ut labore et dolore magna aliqua. Ut enim ad."</p>

    <footer class="abs footer">
      <div class="abs" style="left:17px;top:20px;width:60px">
        <h3>About me.</h3>
        <p>"Lorem ipsum dolor sit amet, consectetur adipiscing elit, sed do eiusmod tempor incididunt</p>
      </div>
      <div class="abs" style="left:95px;top:19px">
        <h3 style="margin-bottom:4px">Legal</h3>
        <ul><li>Privacy policy</li><li>Cookie policy</li><li>Terms and Condition</li></ul>
        <h3 style="margin:5px 0 0">Follow us</h3>
        <div class="social"><i></i><i></i><i></i></div>
      </div>
      <div class="abs" style="left:151px;top:19px">
        <h3>Contact us.</h3>
        <ul class="contact">
          <li><svg width="4" height="4" viewBox="0 0 4 4"><rect x=".8" y=".2" width="2.4" height="3.6" rx=".4" fill="none" stroke="#fff" stroke-width=".4"/></svg><span>000-555-0142-7788<br>000-555-0142-7789</span></li>
          <li><svg width="4" height="4" viewBox="0 0 4 4"><rect x=".2" y=".8" width="3.6" height="2.4" fill="none" stroke="#fff" stroke-width=".4"/><path d="M.2 .8L2 2.2 3.8 .8" fill="none" stroke="#fff" stroke-width=".4"/></svg><span style="font-weight:400">hello@clikora.example</span></li>
        </ul>
      </div>
      <div class="abs logo">LOGO</div>
      <div class="abs copy">Copyright © 2018. All rights reserved.</div>
    </footer>

  </main>
</div>
</body>
</html>
```